Retail Sign for Houseplant Campaign

Please make Portrait style not landscape Sign will measure 3 to 4 foot tall by 22.2inches and place on rolling racks of houseplants for a retail promotion in The Yard Locker. The theme of the promotion will be "Bring your home to life with Houseplants!" Selling points which should be on the sign are Houseplants * improve your mood * reduce fatigue * improve focus. Please put signage in landscape format and include yard locker and verdant makings logo.

Just recovered from covid. Im sorry for the delay

Target Market(s)

People who love plants

Industry/Entity Type

Retail

Colors
00AB8E
00BBA5
67D7C9
C6EFE9
E9F9F6
59FF00
82FF00
B8FF75
E3FFCB
F4FFEA
FFF300
FFF600
FEFA6F
FFFEC7
FFFEE8
FFC000
F8CF3A
FAE287
FDF2CF
FEFAEE

Requirements
Must have
• Must feel energetic and encourage people to buy plants. Should include 1-2 photos and the selling points listed

```html
<!DOCTYPE html>
<html lang="en">
<head>
<meta charset="utf-8">
<title>Bring your home to life with Houseplants – Retail Sign</title>
<link rel="stylesheet" href="https://fonts.googleapis.com/css2?family=Baloo+2:wght@500;600&family=Yellowtail&family=Raleway:wght@400&display=swap">
<style>
  :root {
    --page-bg: #ffffff;
    --sky-top: #7ccdc2;
    --sky-mid: #b5d6c0;
    --sand-bottom: #ddd0a6;
    --ring-teal: #00bba5;
    --ring-light: #e9f9f6;
    --photo-yellow: #f8cf3a;
    --photo-yellow-deep: #ffc000;
    --band-olive: #9f9660;
    --headline-yellow: #f6f06c;
    --gold-light: #f4d95a;
    --gold-dark: #a07a12;
    --points-brown: #8a6a2c;
    --foliage-dark: #2f6b2a;
    --foliage-light: #7fb548;
  }
  * { margin: 0; padding: 0; box-sizing: border-box; }
  html, body { width: 1200px; height: 1200px; overflow: hidden; background: var(--page-bg); }
  .canvas { position: relative; width: 1200px; height: 1200px; }
  .sign {
    position: absolute; left: 377px; top: 116px;
    width: 446px; height: 967px; overflow: hidden;
    background: linear-gradient(170deg, var(--sky-top) 0%, var(--sky-mid) 50%, var(--sand-bottom) 100%);
  }
  .sign-art { position: absolute; inset: 0; }
  .headline { font-weight: normal; }
  .headline-band {
    position: absolute; left: 0; height: 45px;
    background: var(--band-olive);
    border-radius: 0 23px 23px 0;
    padding-left: 9px;
    font-family: "Baloo 2", sans-serif; font-weight: 600;
    font-size: 36px; line-height: 48px; color: var(--headline-yellow);
    letter-spacing: 0.3px; white-space: nowrap;
  }
  .headline-band--first { top: 270px; width: 330px; }
  .headline-band--second { top: 334px; width: 220px; }
  .headline-script {
    position: absolute; left: 0; top: 360px;
    width: 446px; height: 150px; display: block;
  }
  .headline-script text {
    font-family: "Yellowtail", cursive; font-size: 100px;
  }
  .selling-points {
    position: absolute; left: 14px; top: 538px;
    font-family: "Raleway", sans-serif; font-size: 17px;
    color: var(--points-brown); white-space: nowrap;
  }
</style>
</head>
<body>
<main class="canvas">
  <section class="sign">
    <svg class="sign-art" width="446" height="967" viewBox="0 0 446 967">
      <defs>
        <linearGradient id="foliage" x1="0" y1="0" x2="0" y2="1">
          <stop offset="0" stop-color="#7fb548" stop-opacity="0"/>
          <stop offset="0.35" stop-color="#4e8d36"/>
          <stop offset="1" stop-color="#2f6b2a"/>
        </linearGradient>
      </defs>

      <circle cx="86" cy="110" r="86" fill="none" stroke="var(--ring-teal)" stroke-width="2"/>
      <circle cx="80" cy="106" r="84" fill="var(--photo-yellow)" stroke="var(--ring-teal)" stroke-width="3"
              role="img" aria-label="Photo of a smiling woman holding a potted monstera plant"/>

      <circle cx="389" cy="194" r="63" fill="none" stroke="var(--ring-light)" stroke-width="2"/>
      <circle cx="388" cy="196" r="60" fill="var(--photo-yellow-deep)" stroke="var(--ring-teal)" stroke-width="3"
              role="img" aria-label="Photo of an excited woman peeking out from behind palm leaves"/>

      <circle cx="333" cy="698" r="126" fill="none" stroke="var(--ring-light)" stroke-width="2"/>
      <circle cx="330" cy="704" r="120" fill="var(--photo-yellow)" stroke="var(--ring-teal)" stroke-width="3"
              role="img" aria-label="Photo of a woman sitting with a laptop among plants, giving two thumbs up"/>

      <rect x="0" y="770" width="446" height="197" fill="url(#foliage)"
            role="img" aria-label="Photo of lush snake plants and tropical foliage along the bottom edge"/>
    </svg>

    <h1 class="headline">
      <span class="headline-band headline-band--first">Bring your home</span>
      <span class="headline-band headline-band--second">to life with</span>
      <svg class="headline-script" viewBox="0 0 446 150">
        <defs>
          <linearGradient id="gold" x1="0" y1="0" x2="0" y2="1">
            <stop offset="0.2" stop-color="#f4d95a"/>
            <stop offset="1" stop-color="#a07a12"/>
          </linearGradient>
        </defs>
        <text x="34" y="112" transform="rotate(-5 34 112)" fill="url(#gold)"
              textLength="380" lengthAdjust="spacingAndGlyphs">Houseplants!</text>
      </svg>
    </h1>
    <p class="selling-points">* improve your mood * reduce fatigue * improve focus</p>
  </section>
</main>
</body>
</html>
```